New website design for small car detailing company.

We have a small cleaning company, our main focus is car detailing but we are also expanding to home and residential cleaning and power washing.
I would like the web site to have a simple layout and SEO friendly.
I would also like to have a contact page in which clients can contact us and upload pictures of the house or car so we can provide an estimate.
A Page that shows the services we offer.

Target Market(s)

High paying clients for car detailiing and focus on residential and commercial cleaning.

Industry/Entity Type

Cleaning Service

Coding

Coded - Design and coding required

Number of Pages Required

4 page

Font styles to use
Serif

Colors

Designer to choose only greyscale colors for use in the design.

Requirements
Must have
• A home page.
Blog page for SEO
Contact page with the choice of clients to upload theirs pictures so we can provide estimates with calendar integration so they can provide their available dates for service.
A pictures to sell our services.
Nice to have
• Simple but sleek desing, I am more interested in SEO Score than heavy loads

```html
<!DOCTYPE html>
<html lang="en">
<head>
<meta charset="UTF-8">
<title>Harbor Mobile Detailing – Premium Cleaning Service</title>
<link href="https://fonts.googleapis.com/css2?family=Montserrat:wght@400;500;600;700;800&display=swap" rel="stylesheet">
<style>
  :root {
    --ink: #111111;
    --muted: #6f6f6f;
    --white: #ffffff;
    --panel: #141414;
    --panel-grey: #8a8a8a;
    --panel-dim: #6a6a6a;
    --gold: #c89b52;
    --gold-light: #ebcb93;
    --photo-dark: #1c2230;
    --photo-mid: #2c3447;
    --photo-smoke: #6d6e7c;
  }
  * { margin: 0; padding: 0; box-sizing: border-box; }
  html, body { width: 1200px; height: 675px; overflow: hidden; background: var(--white); }
  body { font-family: "Montserrat", sans-serif; color: var(--ink); position: relative; }

  .brand { position: absolute; left: 34px; top: 40px; width: 60px; display: flex; flex-direction: column; align-items: center; gap: 3px; }
  .brand-mark { width: 14px; height: 14px; background: var(--ink); }
  .brand-name { font-size: 6.5px; font-weight: 700; line-height: 1.15; text-align: center; text-transform: uppercase; letter-spacing: .2px; color: var(--ink); }

  .main-nav a { position: absolute; top: 45px; font-size: 14px; font-weight: 600; color: var(--muted); text-decoration: none; letter-spacing: .2px; }
  .main-nav .is-active { color: var(--ink); }
  .main-nav .is-active::after { content: ""; position: absolute; left: 23px; right: -6px; top: 21px; height: 1.5px; background: var(--ink); }

  .menu-toggle { position: absolute; left: 860px; top: 48px; width: 23px; height: 13px; }

  .hero { position: absolute; left: 101px; top: 95px; width: 726px; height: 484px; overflow: hidden; }
  .hero-photo { position: absolute; inset: 0;
    background:
      radial-gradient(ellipse 32% 42% at 64% 62%, #6f7280 0%, rgba(90,92,106,.6) 45%, transparent 80%),
      radial-gradient(ellipse 60% 35% at 75% 95%, rgba(120,118,130,.55), transparent 75%),
      linear-gradient(160deg, var(--photo-mid) 0%, var(--photo-dark) 45%, #23252f 100%); }

  .next-card { position: absolute; left: 51px; top: 36px; width: 130px; height: 94px; display: flex; }
  .next-card-btn { width: 40px; background: var(--white); display: flex; align-items: center; justify-content: center; }
  .next-card-photo { flex: 1; background: linear-gradient(135deg, #3a3a3a, #1c1c1c 60%, #2e2e2e); display: flex; align-items: center; justify-content: center; }
  .next-card-num { font-size: 26px; font-weight: 700; color: var(--gold); opacity: .85; margin-left: -12px; }

  .hero-copy { position: absolute; right: 41px; top: 28px; text-align: right; color: var(--white); }
  .hero-title { font-size: 22px; font-weight: 700; letter-spacing: .1px; }
  .hero-text { margin-top: 7px; font-size: 8.4px; line-height: 9.8px; font-weight: 400; }

  .slide-count { position: absolute; left: 27px; top: 233px; font-size: 13px; font-weight: 600; color: var(--white); }

  .slide-arrows { position: absolute; left: 119px; top: 450px; }
  .slide-dots { position: absolute; left: 317px; top: 455px; display: flex; gap: 8px; }
  .slide-dots span { width: 25px; height: 1.5px; background: rgba(255,255,255,.5); }
  .slide-dots span:first-child { background: var(--white); }

  .hero-actions { position: absolute; left: 506px; top: 445px; display: flex; }
  .btn { width: 90px; height: 21px; font-family: inherit; font-size: 6.6px; font-weight: 500; display: flex; align-items: center; justify-content: center; border: 1px solid var(--white); }
  .btn-solid { background: var(--white); color: var(--ink); }
  .btn-outline { background: transparent; color: var(--white); }

  .slide-index { position: absolute; left: 58px; top: 488px; font-size: 141px; font-weight: 800; line-height: 1; letter-spacing: -6px;
    background: linear-gradient(180deg, var(--gold) 0%, var(--gold-light) 100%); -webkit-background-clip: text; background-clip: text; color: transparent; opacity: .85; }

  .side-panel { position: absolute; left: 918px; top: 0; width: 282px; height: 675px; background: var(--panel); }
  .side-arrow { position: absolute; left: 129px; top: 49px; }
  .side-label { position: absolute; transform: rotate(-90deg); transform-origin: left top; white-space: nowrap; }
  .side-label-main { left: 118px; top: 369px; font-size: 43px; font-weight: 800; color: var(--white); }
  .side-label-sub { left: 126px; top: 509px; font-size: 28px; font-weight: 700; color: var(--panel-grey); }
  .side-label-page { left: 127px; top: 579px; font-size: 18px; font-weight: 700; color: var(--panel-dim); }
</style>
</head>
<body>
  <header>
    <a class="brand" href="#">
      <span class="brand-mark"></span>
      <span class="brand-name">Harbor Mobile Detailing</span>
    </a>
    <nav class="main-nav">
      <a class="is-active" href="#" style="left:101px">Home</a>
      <a href="#" style="left:192px">About Us</a>
      <a href="#" style="left:283px">Services</a>
      <a href="#" style="left:373px">Gallery</a>
    </nav>
    <svg class="menu-toggle" viewBox="0 0 23 13" aria-label="Menu">
      <path d="M0 .75H23M0 6.5H23M0 12.25H23" stroke="#111" stroke-width="1.3"/>
    </svg>
  </header>

  <main>
    <section class="hero">
      <div class="hero-photo" role="img" aria-label="Dark sports car wheel being steam cleaned, surrounded by mist"></div>

      <div class="next-card">
        <div class="next-card-btn">
          <svg width="17" height="8" viewBox="0 0 17 8"><path d="M0 4H16M12.5 .8 16 4l-3.5 3.2" fill="none" stroke="#111" stroke-width="1"/></svg>
        </div>
        <div class="next-card-photo" role="img" aria-label="Detailer polishing a car headlight">
          <span class="next-card-num">02</span>
        </div>
      </div>

      <div class="hero-copy">
        <h1 class="hero-title">Premium Cleaning Service</h1>
        <p class="hero-text">Lorem ipsum dolor sit amet,<br>consectetur adipiscing elit,<br>sed do eiusmod tempor incididunt<br>ut labore et dolore magna aliqua.<br>Ut enim ad minim veniam.</p>
      </div>

      <span class="slide-count">01/03</span>

      <svg class="slide-arrows" width="66" height="12" viewBox="0 0 66 12">
        <path d="M28 6H1M5 2 1 6l4 4" fill="none" stroke="#fff" stroke-width="1.2"/>
        <path d="M37 6H63M59 2l4 4-4 4" fill="none" stroke="#fff" stroke-width="1.2"/>
      </svg>

      <div class="slide-dots"><span></span><span></span><span></span></div>

      <div class="hero-actions">
        <a class="btn btn-solid" href="#">Find Out More</a>
        <a class="btn btn-outline" href="#">Order Now</a>
      </div>
    </section>

    <div class="slide-index">01</div>
  </main>

  <aside class="side-panel">
    <svg class="side-arrow" width="27" height="10" viewBox="0 0 27 10"><path d="M0 5H26M22 1l4 4-4 4" fill="none" stroke="#fff" stroke-width="1.1"/></svg>
    <span class="side-label side-label-main">Car Detailing</span>
    <span class="side-label side-label-sub">Cleaning</span>
    <span class="side-label side-label-page">Home</span>
  </aside>
</body>
</html>
```